Website Revamp: Vormesh.com

Just got a new logo looking for a web design to go with the business. I need the photoshop files and stock photos. No Word Press Please.

```html
<!DOCTYPE html>
<html lang="en">
<head>
<meta charset="utf-8">
<title>Vormesh – Auto Recycling</title>
<link href="https://fonts.googleapis.com/css2?family=Montserrat:wght@400;500;600;700;800&family=Poppins:ital,wght@0,300;0,400;0,500;0,600;1,500&family=Roboto+Condensed:wght@300;400&display=swap" rel="stylesheet">
<style>
:root{
  --green:#8cc63f;
  --green-dark:#76ad2c;
  --ink:#1e1e1e;
  --text:#555;
  --muted:#8a8a8a;
  --ghost:#f1f1f1;
  --footer:#1c1c1c;
  --white:#fff;
}
*{box-sizing:border-box;margin:0;padding:0}
html,body{width:1200px;height:4854px;overflow:hidden}
body{position:relative;background:var(--white);font-family:"Poppins",sans-serif;color:var(--text)}
.abs{position:absolute}
.fill{position:absolute}

/* hero */
.hero{position:absolute;left:0;top:0;width:1200px;height:663px;background:linear-gradient(180deg,#5a6788 0%,#7d6f86 35%,#a2766a 60%,#4a3a36 100%)}
.hero-photo{position:absolute;left:420px;top:110px;width:780px;height:553px;background:radial-gradient(ellipse at 60% 50%,#8a5a4a 0%,#5b4d5a 45%,rgba(60,50,60,0) 75%)}
.brand{position:absolute;left:112px;top:24px;display:flex;align-items:center;gap:12px}
.brand-dot{width:40px;height:40px;border-radius:50%;background:var(--white)}
.brand-name{font-family:"Montserrat",sans-serif;font-weight:700;font-size:24px;color:var(--white)}
.callus{position:absolute;right:112px;top:12px;color:var(--white);font-size:16px;font-family:"Montserrat",sans-serif;display:flex;align-items:center;gap:10px}
.nav-rule{position:absolute;left:0;top:106px;width:1200px;height:1px;background:rgba(255,255,255,.45)}
.nav{position:absolute;left:342px;top:66px;display:flex;gap:0;font-size:14.5px;color:var(--white);font-family:"Montserrat",sans-serif;font-weight:500}
.nav span{padding:0 13px;border-left:1px solid rgba(255,255,255,.8);line-height:15px}
.nav span:first-child{border-left:none;padding-left:0;color:var(--green)}
.nav-active{position:absolute;left:342px;top:104px;width:44px;height:3px;background:var(--green)}
.hero-kicker{position:absolute;left:111px;top:252px;font-family:"Montserrat",sans-serif;font-weight:500;font-size:34px;color:var(--white)}
.hero-title{position:absolute;left:111px;top:292px;font-family:"Montserrat",sans-serif;font-weight:800;font-size:49px;line-height:46px;color:var(--white)}
.btn-ghost{position:absolute;left:111px;top:396px;width:141px;height:43px;border:2px solid var(--white);color:var(--white);font-size:15px;font-family:"Montserrat",sans-serif;font-weight:500;display:flex;align-items:center;justify-content:center}
.arrow-btn{position:absolute;top:368px;width:34px;height:34px;border-radius:50%;border:1px solid rgba(255,255,255,.6);display:flex;align-items:center;justify-content:center}
.dots{position:absolute;left:567px;top:622px;display:flex;gap:7px}
.dots i{width:10px;height:10px;border-radius:50%;background:rgba(255,255,255,.5)}
.dots i:first-child{background:var(--white)}

/* section heads */
.ghost{position:absolute;left:0;width:1200px;text-align:center;font-family:"Montserrat",sans-serif;font-weight:800;font-size:92px;letter-spacing:2px;color:var(--ghost)}
.sec-title{position:absolute;left:0;width:1200px;text-align:center;font-family:"Roboto Condensed",sans-serif;font-weight:400;font-size:40px;color:#3c3c3c}
.sec-title em{font-style:normal;color:var(--green)}
.sec-line{position:absolute;left:570px;width:60px;height:3px;background:var(--green)}
.sec-sub{position:absolute;left:300px;width:600px;text-align:center;font-size:15.5px;line-height:25px;font-weight:500;color:var(--ink)}
.side-label{position:absolute;display:flex;align-items:center;gap:14px;transform-origin:left top;font-family:"Montserrat",sans-serif;font-size:13px;font-weight:600;letter-spacing:2.5px;color:#333;white-space:nowrap}
.side-label::before,.side-label::after{content:"";width:32px;height:2px;background:var(--green)}
.btn-green{position:absolute;height:44px;background:var(--green);color:var(--white);font-family:"Montserrat",sans-serif;font-weight:600;font-size:15px;display:flex;align-items:center;justify-content:center;gap:8px}

/* services */
.help{position:absolute;left:127px;top:966px;font-style:italic;font-weight:500;font-size:15px;color:#666}
.svc-title{position:absolute;left:127px;top:988px;font-family:"Montserrat",sans-serif;font-size:35px;font-weight:500;color:#111}
.svc-line{position:absolute;left:127px;top:1036px;width:56px;height:3px;background:var(--green)}
.svc-text{position:absolute;left:127px;top:1054px;width:438px;font-size:14px;line-height:28.5px;color:#777}

/* who we are */
.who-text{position:absolute;left:625px;top:1616px;width:462px;text-align:center;font-size:14px;line-height:28px;color:#777}

/* stats */
.stats{position:absolute;left:0;top:1918px;width:1200px;height:288px;background:var(--green)}
.stat{position:absolute;top:50px;width:240px;text-align:center;color:var(--white);font-family:"Montserrat",sans-serif}
.stat svg{display:block;margin:0 auto}
.stat b{display:block;margin-top:16px;font-size:21px;font-weight:700}
.stat span{display:block;font-size:17px;line-height:29px;font-weight:400;text-transform:uppercase}

/* projects */
.proj{position:absolute;top:2483px;width:226px;height:324px;border-radius:10px}
.proj-caption{position:absolute;left:16px;bottom:22px;color:var(--white);font-size:13.5px;line-height:26px}

/* video */
.video{position:absolute;left:0;top:2971px;width:1200px;height:445px;background:linear-gradient(135deg,#5d6470 0%,#757a80 50%,#5a5f6a 100%)}
.video-kicker{position:absolute;left:0;top:3102px;width:1200px;text-align:center;font-style:italic;font-weight:500;font-size:15px;color:var(--white)}
.video-title{position:absolute;left:0;top:3126px;width:1200px;text-align:center;font-family:"Montserrat",sans-serif;font-weight:600;font-size:29px;color:var(--white)}
.play{position:absolute;left:553px;top:3182px;width:94px;height:94px;border-radius:50%;background:var(--white);box-shadow:0 0 0 6px rgba(255,255,255,.35);display:flex;align-items:center;justify-content:center}

/* blog */
.social{position:absolute;top:3640px;width:56px;height:56px;border-radius:50%;border:2px solid #555}
.social.active{border-color:var(--green)}
.blog{position:absolute;top:3721px;width:313px;height:281px}
.blog-overlay{position:absolute;inset:0;background:rgba(0,0,0,.45);color:var(--white);text-align:center;font-size:14px;line-height:26px;padding:78px 18px 0}
.blog-meta{margin-top:10px;font-size:13px;display:flex;justify-content:center;gap:30px}

/* map + contact */
.map{position:absolute;left:0;top:4088px;width:1200px;height:490px;background:linear-gradient(180deg,#ececec,#e3e3e3)}
.contact{position:absolute;left:109px;top:4310px;width:980px;height:268px;background:var(--white);border-top:8px solid var(--green);border-radius:22px 22px 0 0}
.c-brand{position:absolute;left:44px;top:46px;display:flex;align-items:center;gap:10px}
.c-dot{width:34px;height:34px;border-radius:50%;background:var(--green)}
.c-name{font-family:"Montserrat",sans-serif;font-weight:700;font-size:24px;color:var(--green)}
.c-row{position:absolute;left:42px;display:flex;align-items:flex-start;gap:14px;color:#111}
.c-msg{position:absolute;left:322px;top:56px;width:260px;font-size:13px;line-height:26px;color:#444}
.c-msg b{color:#111;font-weight:600}
.field{position:absolute;border:1px solid #ccc;font-size:11.5px;color:#999;padding:10px 12px}
.submit{position:absolute;left:776px;top:188px;width:164px;height:38px;background:var(--green);color:var(--white);font-weight:500;font-size:15px;display:flex;align-items:center;justify-content:center}

/* footer */
.footer{position:absolute;left:0;top:4578px;width:1200px;height:276px;background:var(--footer);color:var(--white);font-family:"Montserrat",sans-serif}
.f-col{position:absolute;top:52px;font-size:13.5px;line-height:26px}
.f-col h4{font-size:15px;font-weight:600;margin-bottom:12px;letter-spacing:.3px}
.f-input{position:absolute;left:111px;top:137px;width:239px;height:42px;background:var(--white);color:#999;font-size:13px;padding:12px 10px}
.f-send{position:absolute;left:308px;top:137px;width:42px;height:42px;background:var(--green);display:flex;align-items:center;justify-content:center}
.copy{position:absolute;left:475px;top:242px;font-size:13px}
</style>
</head>
<body>

<!-- Hero -->
<section class="hero">
  <div class="hero-photo" role="img" aria-label="Photo of a tall pile of crushed, colourful scrap cars under a dusk sky"></div>
  <div class="brand"><span class="brand-dot"></span><span class="brand-name">VORMESH</span></div>
  <div class="callus">
    <svg width="18" height="18" viewBox="0 0 24 24" fill="none" stroke="#fff" stroke-width="2"><path d="M22 16.9v3a2 2 0 0 1-2.2 2 19.8 19.8 0 0 1-8.6-3.1 19.5 19.5 0 0 1-6-6A19.8 19.8 0 0 1 2.1 4.2 2 2 0 0 1 4.1 2h3a2 2 0 0 1 2 1.7c.1 1 .4 1.9.7 2.8a2 2 0 0 1-.5 2.1L8 9.9a16 16 0 0 0 6 6l1.3-1.3a2 2 0 0 1 2.1-.4c.9.3 1.8.6 2.8.7a2 2 0 0 1 1.8 2z"/></svg>
    CALL US: 888-888-8888
  </div>
  <nav class="nav"><span>Home</span><span>About</span><span>Service</span><span>Parts And Inventory</span><span>Listing Of Used Cars</span><span>Gallery</span><span>Contact Us</span></nav>
  <div class="nav-rule"></div>
  <div class="nav-active"></div>
  <div class="hero-kicker">VORMESH</div>
  <h1 class="hero-title">SPECIFCALLY WITH<br>AUTO RECYCLING</h1>
  <div class="btn-ghost">Get Started</div>
  <div class="arrow-btn" style="left:44px"><svg width="12" height="12" viewBox="0 0 12 12"><path d="M8 1L3 6l5 5" fill="none" stroke="#fff" stroke-width="1.6"/></svg></div>
  <div class="arrow-btn" style="left:1114px"><svg width="12" height="12" viewBox="0 0 12 12"><path d="M4 1l5 5-5 5" fill="none" stroke="#fff" stroke-width="1.6"/></svg></div>
  <div class="dots"><i></i><i></i><i></i><i></i></div>
</section>

<!-- Services -->
<div class="ghost" style="top:730px">SERVICES</div>
<h2 class="sec-title" style="top:774px">OUR <em>SERVICES</em></h2>
<div class="sec-line" style="top:826px"></div>
<p class="sec-sub" style="top:844px">Lorem ipsum dolor sit amet, consectetur adipiscing elit, sed do eiusmod cididunt ut labore et dolore magna aliqua.</p>

<div class="side-label" style="left:78px;top:1272px;transform:rotate(-90deg)">AUTO RECYCLING</div>
<p class="help">How can we help?</p>
<h3 class="svc-title">AUTO RECYCLING</h3>
<div class="svc-line"></div>
<p class="svc-text">Lorem ipsum dolor sit amet, consectetur adipiscing elit, sed do eiusmod tempor incididunt ut labore et dolore magna aliqua. Quis ipsum suspendisse ultrices gravida. Risus modo viverra maecenas accumsan lacus vel facilisis. Lorem ipsum dolor sit amet, consectetur adipiscing elit, seusmod tempor incididunt ut labore et dolore magna aliqua.</p>
<div class="btn-green" style="left:127px;top:1257px;width:218px">View Our Services <svg width="16" height="10" viewBox="0 0 16 10"><path d="M0 5h13M9 1l4 4-4 4" fill="none" stroke="#fff" stroke-width="2"/></svg></div>

<div class="fill" style="left:606px;top:928px;width:148px;height:140px;background:var(--green)"></div>
<div class="fill" style="left:641px;top:963px;width:465px;height:380px;background:#cfcfcf"></div>
<div class="fill" role="img" aria-label="Photo of a crane claw lifting a red wrecked car over a scrap pile against a blue sky" style="left:624px;top:946px;width:465px;height:380px;background:linear-gradient(180deg,#3f6fb3 0%,#7aa2d2 45%,#8a6f6a 70%,#b9b7b5 100%)"></div>

<!-- Who we are -->
<div class="fill" role="img" aria-label="Photo of damaged cars parked in a wooded salvage yard" style="left:0;top:1422px;width:600px;height:496px;background:linear-gradient(160deg,#59644a 0%,#3d4136 45%,#8e8f8c 75%,#5b5c5a 100%)"></div>
<div class="fill" style="left:600px;top:1422px;width:600px;height:496px;background:linear-gradient(180deg,#f4f4f4,#ebebeb)"></div>
<div class="ghost" style="top:1498px;left:300px;color:#e6e6e6">ABOUT</div>
<h2 class="sec-title" style="top:1538px;left:300px">WHO <em>WE ARE</em></h2>
<div class="sec-line" style="top:1590px;left:828px"></div>
<p class="who-text">Lorem ipsum dolor sit amet, consectetur adipiscing elit, sedmod tempor incididunt ut labore et dolore magna aliquasum pendisse ultrices gravida. Risus commodo viverracenas cumsan lacus vel facilisis. Lorem ipsum dolor sit amet, tur ascing elit, sed do eiusmod tempor incididunt ut labore Risus coumsan lacus vel facilisis.</p>
<div class="btn-green" style="left:772px;top:1784px;width:168px">Learn More <svg width="16" height="10" viewBox="0 0 16 10"><path d="M0 5h13M9 1l4 4-4 4" fill="none" stroke="#fff" stroke-width="2"/></svg></div>
<div class="side-label" style="left:1123px;top:1556px;transform:rotate(90deg)">ABOUT COMPANY</div>

<!-- Stats -->
<section class="stats">
  <div class="stat" style="left:93px">
    <svg width="98" height="98" viewBox="0 0 98 98" fill="none" stroke="#fff" stroke-width="2"><circle cx="49" cy="49" r="47"/><path d="M30 70V34h14v36M44 70V26h16v44M60 70V44h10v26M26 70h46M34 40h6M34 48h6M34 56h6M48 32h8M48 40h8M48 48h8M48 56h8"/></svg>
    <b>2020</b><span>Year<br>Established</span>
  </div>
  <div class="stat" style="left:338px">
    <svg width="98" height="98" viewBox="0 0 98 98" fill="none" stroke="#fff" stroke-width="2"><circle cx="49" cy="49" r="47"/><path d="M34 26h22l10 10v36H34zM56 26v10h10M40 44h20M40 52h20M40 60h14"/></svg>
    <b>2000+</b><span>Projects<br>Completed</span>
  </div>
  <div class="stat" style="left:607px">
    <svg width="98" height="98" viewBox="0 0 98 98" fill="none" stroke="#fff" stroke-width="2"><circle cx="49" cy="49" r="47"/><path d="M49 26l-10 17M39 43l-6-3M39 43l1-7M60 46l10 17H58M58 63l4 5M58 63l4-5M28 63l10-17M38 46l-7 1M38 46l4 6M49 26l8 14"/></svg>
    <b>100%</b><span>Target Recycled<br>Waste Stream</span>
  </div>
  <div class="stat" style="left:873px">
    <svg width="98" height="98" viewBox="0 0 98 98" fill="none" stroke="#fff" stroke-width="2"><circle cx="49" cy="49" r="47"/><circle cx="49" cy="45" r="10"/><circle cx="49" cy="45" r="17" stroke-dasharray="6 5"/><path d="M38 72h22M44 66h10"/></svg>
    <b>75+</b><span>Pieces of<br>Equipment</span>
  </div>
</section>

<!-- Projects -->
<div class="ghost" style="top:2314px">PROJECTS</div>
<h2 class="sec-title" style="top:2336px">OUR <em>PROJECTS</em></h2>
<div class="sec-line" style="top:2388px"></div>
<p class="sec-sub" style="top:2404px">Lorem ipsum dolor sit amet, consectetur adipiscing elit, sed do eiusmod cididunt ut labore et dolore magna aliqua.</p>
<div class="side-label" style="left:69px;top:2745px;transform:rotate(-90deg)">RECYCLING PROJECTS</div>

<div class="proj" role="img" aria-label="Photo of an excavator loading scrap into a blue container" style="left:109px;background:linear-gradient(180deg,#6d7f9a,#3d4f6a 60%,#2b2f3a)">
  <svg class="abs" style="left:95px;top:138px" width="36" height="36" viewBox="0 0 36 36" fill="none" stroke="#fff" stroke-width="2"><circle cx="18" cy="18" r="16"/><path d="M11 18h13M19 13l5 5-5 5"/></svg>
  <p class="proj-caption">Lorem ipsum dolor sit amet,<br>consectetur adipiscing</p>
</div>
<div class="proj" role="img" aria-label="Photo of stacked crushed car bales" style="left:360px;background:linear-gradient(180deg,#6f5a4c,#8a4f3a 50%,#4f4a4a)"></div>
<div class="proj" role="img" aria-label="Photo of a red wrecked car on a scrap heap" style="left:610px;background:linear-gradient(180deg,#9aa0a5,#8a5a58 50%,#7c7d80)"></div>
<div class="proj" role="img" aria-label="Photo of a pile of mangled cars under a blue sky" style="left:861px;background:linear-gradient(180deg,#5f8ec4,#4a5f7a 50%,#6a4a4a)"></div>

<div class="btn-green" style="left:497px;top:2839px;width:206px">View All Projects <svg width="16" height="10" viewBox="0 0 16 10"><path d="M0 5h13M9 1l4 4-4 4" fill="none" stroke="#fff" stroke-width="2"/></svg></div>

<!-- Video -->
<section class="video" role="img" aria-label="Aerial photo of rows of parked cars in a large salvage lot"></section>
<p class="video-kicker">How do we work?</p>
<h2 class="video-title">WATCH FOR YOURSELF</h2>
<div class="play"><svg width="30" height="34" viewBox="0 0 30 34"><path d="M4 2l24 15L4 32z" fill="#111"/></svg></div>

<!-- Blog -->
<div class="ghost" style="top:3478px">SOCIAL BLOG</div>
<h2 class="sec-title" style="top:3502px;color:#111">SOCIAL <em>BLOG</em></h2>
<div class="sec-line" style="top:3554px"></div>
<p class="sec-sub" style="top:3570px">Lorem ipsum dolor sit amet, consectetur adipiscing elit, sed do eiusmod cididunt ut labore et dolore magna aliqua.</p>

<div class="social active" style="left:469px" aria-label="Friendbook"></div>
<div class="social" style="left:537px" aria-label="Chirper"></div>
<div class="social" style="left:605px" aria-label="Netlink"></div>
<div class="social" style="left:673px" aria-label="Snapwall"></div>
<svg class="abs" style="left:1032px;top:3673px" width="56" height="28" viewBox="0 0 56 28" fill="none" stroke-width="1.6"><circle cx="14" cy="14" r="12" stroke="#333"/><path d="M17 9l-5 5 5 5" stroke="#333"/><circle cx="42" cy="14" r="12" stroke="#8cc63f"/><path d="M39 9l5 5-5 5" stroke="#8cc63f"/></svg>

<div class="blog" role="img" aria-label="Photo of a pile of old tyres" style="left:109px;background:linear-gradient(180deg,#4b4b4b,#1e1e1e)">
  <div class="blog-overlay">Lorem ipsum dolor sit amet, consectetur adipiscing elit, sed do eiusmod tempor incididunt ut labore et dolor
    <div class="blog-meta"><span>&#9825; 277</span><span>&#9679; 22</span></div>
  </div>
</div>
<div class="blog" role="img" aria-label="Photo of rusty cars stacked on shelving racks" style="left:443px;background:linear-gradient(180deg,#a86a3e,#7a4a36 50%,#c8b8a8)"></div>
<div class="blog" role="img" aria-label="Photo of a loader grabbing a red car at a scrapyard" style="left:774px;background:linear-gradient(180deg,#5a7fb8,#8e8a8c 55%,#b4a06a)"></div>

<!-- Map + contact -->
<div class="map" role="img" aria-label="Street map around the yard location"></div>
<section class="contact">
  <div class="c-brand"><span class="c-dot"></span><span class="c-name">VORMESH</span></div>
  <div class="c-row" style="top:132px">
    <svg width="22" height="28" viewBox="0 0 22 28" fill="none" stroke="#444" stroke-width="1.8"><path d="M11 26s9-9 9-15a9 9 0 0 0-18 0c0 6 9 15 9 15z"/><circle cx="11" cy="11" r="3"/></svg>
    <div><div style="font-weight:600;font-size:15px">1234 Lorem Ipsum</div><div style="font-size:13px;color:#333">Port Loctor NY -lyl</div></div>
  </div>
  <div class="c-row" style="top:198px;align-items:center">
    <svg width="22" height="28" viewBox="0 0 22 28" fill="none" stroke="#444" stroke-width="1.8"><rect x="4" y="2" width="14" height="24" rx="2"/><path d="M9 22h4"/></svg>
    <div style="font-weight:600;font-size:16px;font-family:Montserrat,sans-serif">888-888-8888</div>
  </div>
  <p class="c-msg"><b>We're always happy</b> to hear from you,whether you're regular customer or just inquiring about our services</p>
  <p class="c-msg" style="top:148px;font-size:12px;color:#111">Thanks for your interest in Vormesh</p>
  <p class="c-msg" style="top:204px;font-size:12px">Let us know how we can help</p>
  <div class="field" style="left:601px;top:53px;width:166px;height:38px">Name</div>
  <div class="field" style="left:778px;top:53px;width:162px;height:38px">Email</div>
  <div class="field" style="left:601px;top:100px;width:339px;height:76px">Message</div>
  <div class="submit">Submit</div>
</section>

<!-- Footer -->
<footer class="footer">
  <div class="f-col" style="left:111px;width:250px"><h4>REGISTER FOR UPDATES</h4>Lorem ipsum dour adipiscing elit, sed do eiusmod tempor</div>
  <div class="f-input">Email</div>
  <div class="f-send"><svg width="18" height="18" viewBox="0 0 24 24" fill="none" stroke="#fff" stroke-width="2"><path d="M22 2L11 13M22 2l-7 20-4-9-9-4z"/></svg></div>
  <div class="f-col" style="left:475px"><h4>ABOUT US</h4>Careers<br>Portfolio<br>Reviews<br>Service Area<br>Contact Us</div>
  <div class="f-col" style="left:684px"><h4>FOLLOW US</h4>Netlink<br>Snapwall<br>Friendbook<br>Chirper</div>
  <div class="f-col" style="left:895px"><h4>HOURS OF OPERATION</h4>
    <div style="display:grid;grid-template-columns:62px auto;font-size:13px">
      <span>Mon-Fri</span><span>08:00 AM - 05:30 PM</span>
      <span>Sat</span><span>09:00 AM - 12:30 PM</span>
      <span>Sun</span><span>Closed</span>
    </div>
  </div>
  <p class="copy">Copyright © 2020. All Rights Reserved</p>
</footer>

</body>
</html>
```